Business card and stationary package

Travel management company looking for designs for single sided business cards, letterhead and envelope. Looking for contemporary designs using our existing logo. Design should clean, not trendy, no gradation of colors and no graphic other than the icon from the logo. Nothing complicated or difficult to read. Should be a crisp design using blue, gray and black colors only.
Letterhead should include a Word template and PDF template.
Business cards are one sided as the reverse will be dynamic images in our company portfolio of images.
We will use the same designer periodically for design projects using the same style guide for upcoming projects as well. Prefer working with designer that will assist with website, brochures and other marketing materials.

Logo Colors and Font:
Blue: 2189c6 Color Hex
Gray: 666666 Color Hex 60% Black
Black: 100% Black
Font: Century Gothic

Target Market(s)

business-to-business

Industry/Entity Type

Travel Industry

Contact Information for Business Card

Sample information for business cards will be:

Daniel Ferris
Managing Partner

Bluefield Journey Services, Inc.
47 Alder Lane, Suite 2204
Harlow, ME 04196

207-555-0148 Direct Dial
207-555-0149 Fax

daniel@bluefieldjourney.net
www.bluefieldjourney.net

Font styles to use
Sans Serif

Requirements
Must have
• Clean, crisp design, easy to ready, memorable.
Nice to have
• We tend to like dynamic designs that are simple, not trendy, contemporary and easy to read.
Should not have
• no gradation of colors and no graphic other than the icon from the logo, no background images
• **Note that the background should only be white. No black/gary backgrounds or graded colors**

```html
<!DOCTYPE html>
<html lang="en">
<head>
<meta charset="utf-8">
<title>Bluefield Journey Services – Stationery Package</title>
<link rel="stylesheet" href="https://fonts.googleapis.com/css2?family=Didact+Gothic&family=Montserrat:wght@500;600&display=swap">
<style>
  :root{
    --brand-blue:#2189c6;
    --brand-gray:#666666;
    --ink:#000000;
    --text-gray:#6b6b6b;
    --paper:#ffffff;
    --card-alt:#f7f7f7;
    --flap:#666363;
    --board:#b4b5b7;
  }
  *{box-sizing:border-box;margin:0;padding:0}
  html,body{width:1200px;height:1200px;overflow:hidden}
  body{background:var(--board);font-family:"Didact Gothic",sans-serif;color:var(--text-gray);position:relative}
  .label{position:absolute;font-family:"Montserrat",sans-serif;font-weight:600;font-size:13px;color:#222;transform:translateX(-50%);white-space:nowrap}
  .sheet{position:absolute;background:var(--paper);box-shadow:0 6px 8px rgba(0,0,0,.18)}
  .brand{position:absolute;display:flex;align-items:center;gap:7px;white-space:nowrap}
  .brand-dot{border-radius:50%;background:var(--brand-blue);flex:none}
  .brand-name{color:var(--brand-gray);font-family:"Didact Gothic",sans-serif;letter-spacing:.5px}
  .icon{width:15px;height:15px;flex:none}
  .contact{position:absolute;display:flex;gap:5px;align-items:flex-start;font-size:8.6px;line-height:11px;color:var(--text-gray);white-space:nowrap}
  .contact small{font-size:5.5px}
  .contact .right{text-align:right}
  .link{color:var(--brand-blue)}
  .letter-body{position:absolute;left:60px;top:128px;width:317px;font-family:"Montserrat",sans-serif;font-weight:500;font-size:6.4px;line-height:11.4px;text-align:justify;color:#707070}
  .letter-body p{margin-bottom:6px}
  .signature{position:absolute;left:62px;top:369px;width:55px;height:22px;background:#e6e6e6;border-radius:2px}
  .signer{position:absolute;left:63px;top:393px;font-family:"Montserrat",sans-serif;font-weight:500;font-size:6.8px;line-height:12.5px;color:#777}
  .flap{position:absolute;display:block}
  .card-name{position:absolute;left:94px;top:17px;font-size:9.5px;color:var(--brand-gray);border-bottom:1px solid var(--brand-gray);padding-bottom:1px}
  .card-name b{color:var(--brand-blue);font-weight:normal}
  .card-title{font-size:5px;display:block;letter-spacing:.2px}
  .card-contact{position:absolute;left:92px;display:flex;gap:3px;font-size:4.3px;line-height:5.4px;color:#555;white-space:nowrap}
  .card-contact .icon{width:8px;height:8px}
</style>
</head>
<body>
<svg width="0" height="0" style="position:absolute">
  <symbol id="i-phone" viewBox="0 0 20 20"><circle cx="10" cy="10" r="10" fill="#666"/><path d="M4.5 9.5c0-2.2 2.5-3.5 5.5-3.5s5.5 1.3 5.5 3.5l-2.2.6-.5-1.6h-5.6l-.5 1.6z M6.5 11h7l1 3.5h-9z" fill="#fff"/><circle cx="10" cy="12.6" r="1.2" fill="#666"/></symbol>
  <symbol id="i-web" viewBox="0 0 20 20"><circle cx="10" cy="10" r="10" fill="#666"/><circle cx="10" cy="10" r="5.5" fill="none" stroke="#fff" stroke-width="1.3"/><circle cx="10" cy="10" r="2" fill="none" stroke="#fff" stroke-width="1.3"/></symbol>
  <symbol id="i-pin" viewBox="0 0 20 20"><circle cx="10" cy="10" r="10" fill="#666"/><path d="M10 4a4 4 0 0 0-4 4c0 3 4 8 4 8s4-5 4-8a4 4 0 0 0-4-4z" fill="#fff"/><circle cx="10" cy="8" r="1.5" fill="#666"/></symbol>
</svg>

<!-- Letterhead -->
<div class="label" style="left:304px;top:58px">A4 Letterhead</div>
<section class="sheet letterhead" style="left:102px;top:85px;width:437px;height:584px">
  <div class="brand" style="left:62px;top:28px"><span class="brand-dot" style="width:28px;height:28px"></span><span class="brand-name" style="font-size:17px">BLUEFIELD JOURNEY</span></div>
  <div class="contact" style="left:272px;top:40px"><svg class="icon"><use href="#i-phone"/></svg><span class="right"><small>Direct Dial</small> 207-555-0148<br><small>Fax</small> 207-555-0149</span></div>
  <div class="letter-body">
    <p>Dear (Name)–</p>
    <p>This is a sample letter that has been placed to demonstrate the typing format on the ( Your Company) letter head design. When positioned properly, it will serve to work in harmony with all of other elements on the letterhead</p>
    <p>This letterhead design is meant to project an image of professionalism and reliabilty. By using simple alignments we have created a very spacious feeling. The simplicty suggests strength and the spaciousness contributors to the aesthetics of the layout. These basic qualities along with the (Your Company) colours are consistent with the overall look and helps to reinforce the (Your Company) brand. This letterhead design is meant to project an image of professionalism and reliability.</p>
    <p>This letterhead design is based on the (Form of your logo) form the (Your Company) logo Each stationery has a part of the (Form of your logo)</p>
    <p style="margin-top:26px">Sincerely yours,</p>
  </div>
  <div class="signature" role="img" aria-label="Handwritten signature"></div>
  <div class="signer">Alan Pierce<br>Post Title</div>
  <div class="contact" style="left:62px;top:532px"><svg class="icon"><use href="#i-web"/></svg><span>daniel@bluefieldjourney.net<br>www.<span class="link">bluefieldjourney</span>.net</span></div>
  <div class="contact" style="left:214px;top:532px"><svg class="icon"><use href="#i-pin"/></svg><span>Bluefield Journey Services, Inc.<br>47 Alder Lane, Suite 2204<br>Harlow, ME 04196</span></div>
</section>

<!-- A4 envelope -->
<div class="label" style="left:856px;top:58px">envelope a4 (23x32.5 cm)</div>
<section class="envelope-a4" style="position:absolute;left:602px;top:86px;width:476px;height:775px">
  <svg class="flap" style="left:0;top:0" width="476" height="102" viewBox="0 0 476 102"><path d="M0 102 L14 22 Q18 0 42 0 L434 0 Q458 0 462 22 L476 102 Z" fill="var(--flap)"/></svg>
  <div class="sheet" style="left:0;top:101px;width:476px;height:674px">
    <div class="brand" style="left:35px;top:46px"><span class="brand-dot" style="width:36px;height:36px"></span><span class="brand-name" style="font-size:20px">BLUEFIELD JOURNEY</span></div>
    <div class="contact" style="left:35px;top:621px"><svg class="icon"><use href="#i-phone"/></svg><span class="right"><small>Direct Dial</small> 207-555-0148<br><small>Fax</small> 207-555-0149</span></div>
    <div class="contact" style="left:140px;top:621px"><svg class="icon"><use href="#i-web"/></svg><span>daniel@bluefieldjourney.net<br>www.<span class="link">bluefieldjourney</span>.net</span></div>
    <div class="contact" style="left:284px;top:621px"><svg class="icon"><use href="#i-pin"/></svg><span>Bluefield Journey Services, Inc.<br>47 Alder Lane, Suite 2204<br>Harlow, ME 04196</span></div>
  </div>
</section>

<!-- Business card -->
<div class="label" style="left:290px;top:717px">business card</div>
<section class="sheet card-front" style="left:104px;top:742px;width:186px;height:105px">
  <div class="card-name"><b>Daniel</b> Ferris<span class="card-title">MANAGING PARTNER</span></div>
  <div class="brand" style="left:10px;top:46px;gap:4px"><span class="brand-dot" style="width:14px;height:14px"></span><span class="brand-name" style="font-size:8px;letter-spacing:.2px">BLUEFIELD</span></div>
  <div class="card-contact" style="top:49px"><svg class="icon"><use href="#i-phone"/></svg><span>207-555-0148 Direct Dial<br>207-555-0149 Fax</span></div>
  <div class="card-contact" style="top:61px"><svg class="icon"><use href="#i-web"/></svg><span>daniel@bluefieldjourney.net<br>www.<span class="link">bluefieldjourney</span>.net</span></div>
  <div class="card-contact" style="top:73px"><svg class="icon"><use href="#i-pin"/></svg><span>Bluefield Journey Services, Inc.<br>47 Alder Lane, Suite 2204<br>Harlow, ME 04196</span></div>
</section>
<section class="sheet card-back" style="left:307px;top:742px;width:185px;height:105px;background:var(--card-alt)">
  <div class="brand" style="left:42px;top:38px"><span class="brand-dot" style="width:26px;height:26px"></span><span class="brand-name" style="font-size:13px">BLUEFIELD</span></div>
</section>

<!-- 9x4 envelope front -->
<div class="label" style="left:335px;top:890px">envelope 9’x4’ (Front)</div>
<section class="sheet envelope-front" style="left:107px;top:912px;width:475px;height:219px">
  <div class="brand" style="left:36px;top:19px"><span class="brand-dot" style="width:32px;height:32px"></span><span class="brand-name" style="font-size:18px">BLUEFIELD JOURNEY</span></div>
  <div class="contact" style="left:35px;top:173px"><svg class="icon"><use href="#i-phone"/></svg><span class="right"><small>Direct Dial</small> 207-555-0148<br><small>Fax</small> 207-555-0149</span></div>
  <div class="contact" style="left:149px;top:172px"><svg class="icon"><use href="#i-web"/></svg><span>daniel@bluefieldjourney.net<br>www.bluefieldjourney.net</span></div>
  <div class="contact" style="left:284px;top:172px"><svg class="icon"><use href="#i-pin"/></svg><span>Bluefield Journey Services, Inc.<br>47 Alder Lane, Suite 2204<br>Harlow, ME 04196</span></div>
</section>

<!-- 9x4 envelope back -->
<div class="label" style="left:879px;top:890px">envelope 9’x4’ (back)</div>
<section class="sheet envelope-back" style="left:637px;top:912px;width:475px;height:219px">
  <svg class="flap" style="left:0;top:0" width="475" height="52" viewBox="0 0 475 52"><path d="M0 0 L475 0 L469 34 Q466 52 448 52 L27 52 Q9 52 6 34 Z" fill="var(--flap)"/></svg>
  <div class="brand" style="left:150px;top:94px"><span class="brand-dot" style="width:36px;height:36px"></span><span class="brand-name" style="font-size:19px">BLUEFIELD</span></div>
</section>
</body>
</html>
```